Website R86 coffee

I am opening a small business selling locally roasted coffee online. To start with I want a site with three pages. 1. A welcome page with logo and mission/vision. 2. Shopping/ordering page. 3. About Us page. The brand is "R86 Coffee - A warm start to every day". We are giving back to the downs syndrome community by employing people with down syndrome (Trisomy 21) and buy donating to down syndrome research.

Target Market(s)

Families and friends of people with downs syndrome

Coding

Coded - Design and coding required

Number of Pages Required

3 page

```html
<!DOCTYPE html>
<html lang="en">
<head>
<meta charset="utf-8">
<title>R86 Coffee – Shopping</title>
<link rel="stylesheet" href="https://fonts.googleapis.com/css2?family=Poppins:wght@300;400;500;600&display=swap">
<style>
:root{
  --bg:#232324;
  --smoke:#4a4a4c;
  --card:#1b1b1c;
  --text:#e6e6e6;
  --text-soft:#bdbdbd;
  --text-muted:#a8a8a8;
  --accent-line:#8a8a8a;
  --btn-light:#e4e4e4;
  --btn-dark:#a9a9a9;
  --btn-text:#1e1e1e;
  --photo-light:#d9d6d2;
  --photo-warm:#9a7452;
}
*{margin:0;padding:0;box-sizing:border-box}
html,body{width:1200px;height:844px;overflow:hidden}
body{font-family:"Poppins",sans-serif;color:var(--text);background:var(--bg);position:relative}
.backdrop{position:absolute;inset:0;
  background:
    radial-gradient(ellipse 420px 160px at 200px 780px,rgba(120,120,122,.45),transparent 70%),
    radial-gradient(ellipse 500px 180px at 900px 800px,rgba(110,110,112,.4),transparent 70%),
    radial-gradient(ellipse 300px 260px at 1000px 300px,rgba(70,70,72,.35),transparent 70%),
    linear-gradient(180deg,var(--bg) 0%,#1f1f20 60%,var(--smoke) 100%);}
.site-header{position:absolute;top:0;left:0;width:1200px;height:140px}
.brand{position:absolute;left:89px;top:12px;width:116px;height:116px;display:flex;align-items:center;justify-content:center;gap:6px}
.brand-mark{width:8px;height:8px;background:var(--text)}
.brand-name{font-size:17px;font-weight:400;color:var(--text);letter-spacing:.5px}
.main-nav{position:absolute;top:38px;left:658px;display:flex;gap:32px;font-size:15px;font-weight:400}
.main-nav a{color:var(--text);text-decoration:none;position:relative;padding-bottom:10px}
.main-nav a.is-active{color:var(--text-muted)}
.main-nav a.is-active::after{content:"";position:absolute;left:-2px;right:-6px;bottom:-3px;height:2px;background:var(--accent-line)}
.cart-link{position:absolute;left:1079px;top:40px;width:22px;height:24px}
.cart-count{position:absolute;left:15px;top:-6px;width:15px;height:15px;border-radius:50%;background:#8f8f8f;color:#1b1b1b;font-size:10px;font-weight:600;display:flex;align-items:center;justify-content:center}
.page-intro{position:absolute;top:174px;width:1200px;text-align:center}
.page-title{font-size:46px;font-weight:300;letter-spacing:1px;color:var(--text);line-height:1.2}
.page-lead{font-size:16px;font-weight:300;color:var(--text);margin-top:0}
.products{position:absolute;top:313px;left:89px;display:flex;gap:11px}
.product{position:relative;width:247px;height:344px;background:var(--card);text-align:center}
.product-photo{position:absolute;left:38px;top:-26px;width:170px;height:166px;
  background:linear-gradient(160deg,var(--photo-light) 0%,var(--photo-warm) 100%)}
.product-name{position:absolute;top:170px;width:100%;font-size:19px;font-weight:300;color:var(--text)}
.product-desc{position:absolute;top:198px;width:100%;font-size:13px;font-weight:300;color:var(--text-soft);line-height:17px}
.product-price{position:absolute;top:240px;width:100%;font-size:19px;font-weight:300;color:var(--text)}
.add-to-cart{position:absolute;top:274px;left:50%;margin-left:-87px;width:174px;height:37px;border:0;
  background:linear-gradient(90deg,var(--btn-light),var(--btn-dark));color:var(--btn-text);
  font-family:"Poppins",sans-serif;font-size:14px;font-weight:600;display:flex;align-items:center;justify-content:center;gap:4px}
.site-footer{position:absolute;top:790px;width:1200px;text-align:center;font-size:16px;font-weight:300;color:var(--text)}
</style>
</head>
<body>
<div class="backdrop" role="img" aria-label="Dark backdrop with drifting coffee steam"></div>

<header class="site-header">
  <div class="brand"><span class="brand-mark"></span><span class="brand-name">R86 Coffee</span></div>
  <nav class="main-nav">
    <a href="#">HOME</a>
    <a href="#">ABOUT US</a>
    <a href="#" class="is-active">SHOPPING</a>
    <a href="#">CONTACT US</a>
  </nav>
  <a class="cart-link" href="#" aria-label="Cart">
    <svg width="20" height="22" viewBox="0 0 20 22" fill="none" stroke="#e6e6e6" stroke-width="1.4">
      <path d="M2 6h16l-1 15H3z"/><path d="M6 8V4a4 4 0 0 1 8 0v4"/>
    </svg>
    <span class="cart-count">0</span>
  </a>
</header>

<section class="page-intro">
  <h1 class="page-title">SHOPPING</h1>
  <p class="page-lead">Lorem Ipsum is simply dummy text of the printing and typesetting industry.</p>
</section>

<main class="products">
  <article class="product">
    <div class="product-photo" role="img" aria-label="Photo of a cappuccino cup seen from above"></div>
    <h2 class="product-name">HEADING HERE 1</h2>
    <p class="product-desc">Lorem Ipsum is simply dummy<br>text of the printing .</p>
    <p class="product-price">$9.00</p>
    <button class="add-to-cart"><svg width="16" height="16" viewBox="0 0 24 24" fill="#1e1e1e"><path d="M7 18a2 2 0 1 0 0 4 2 2 0 0 0 0-4zm10 0a2 2 0 1 0 0 4 2 2 0 0 0 0-4zM1 2h3.3l.9 2H21l-3.6 7.5H8.1L7.2 13H19v2H4l2.3-4.2L3 4H1z"/></svg>ADD TO CART</button>
  </article>
  <article class="product">
    <div class="product-photo" role="img" aria-label="Photo of a mocha cup with heart latte art seen from above"></div>
    <h2 class="product-name">HEADING HERE 2</h2>
    <p class="product-desc">Lorem Ipsum is simply dummy<br>text of the printing .</p>
    <p class="product-price">$9.00</p>
    <button class="add-to-cart"><svg width="16" height="16" viewBox="0 0 24 24" fill="#1e1e1e"><path d="M7 18a2 2 0 1 0 0 4 2 2 0 0 0 0-4zm10 0a2 2 0 1 0 0 4 2 2 0 0 0 0-4zM1 2h3.3l.9 2H21l-3.6 7.5H8.1L7.2 13H19v2H4l2.3-4.2L3 4H1z"/></svg>ADD TO CART</button>
  </article>
  <article class="product">
    <div class="product-photo" role="img" aria-label="Photo of a latte cup with leaf art seen from above"></div>
    <h2 class="product-name">HEADING HERE 3</h2>
    <p class="product-desc">Lorem Ipsum is simply dummy<br>text of the printing .</p>
    <p class="product-price">$9.00</p>
    <button class="add-to-cart"><svg width="16" height="16" viewBox="0 0 24 24" fill="#1e1e1e"><path d="M7 18a2 2 0 1 0 0 4 2 2 0 0 0 0-4zm10 0a2 2 0 1 0 0 4 2 2 0 0 0 0-4zM1 2h3.3l.9 2H21l-3.6 7.5H8.1L7.2 13H19v2H4l2.3-4.2L3 4H1z"/></svg>ADD TO CART</button>
  </article>
  <article class="product">
    <div class="product-photo" role="img" aria-label="Photo of a flat white cup dusted with cocoa seen from above"></div>
    <h2 class="product-name">HEADING HERE 4</h2>
    <p class="product-desc">Lorem Ipsum is simply dummy<br>text of the printing .</p>
    <p class="product-price">$9.00</p>
    <button class="add-to-cart"><svg width="16" height="16" viewBox="0 0 24 24" fill="#1e1e1e"><path d="M7 18a2 2 0 1 0 0 4 2 2 0 0 0 0-4zm10 0a2 2 0 1 0 0 4 2 2 0 0 0 0-4zM1 2h3.3l.9 2H21l-3.6 7.5H8.1L7.2 13H19v2H4l2.3-4.2L3 4H1z"/></svg>ADD TO CART</button>
  </article>
</main>

<footer class="site-footer">©Copyright R86 All Rights Reserved</footer>
</body>
</html>
```